Business Card Design Project

We consult with hotels on setting rates and maximizing a revenue strategy

Industry/Entity Type

Business

Contact Information for Business Card

I am not sure what I want. Our company offers high level consulting to hotels around the country but we are also laid back. I would like something that is professional but also shows the laid back side

```html
<!DOCTYPE html>
<html lang="en">
<head>
<meta charset="utf-8">
<title>Harborline Revenue Management Solutions – Business Card</title>
<link href="https://fonts.googleapis.com/css2?family=Arimo:wght@400;700&display=swap" rel="stylesheet">
<style>
  :root {
    --page-bg: #ececec;
    --card-bg: #35231d;
    --card-text: #f4f1ee;
    --accent-teal: #1f8a80;
  }
  html, body {
    margin: 0;
    padding: 0;
    width: 1200px;
    height: 1200px;
    overflow: hidden;
    background: var(--page-bg);
    font-family: "Arimo", Arial, sans-serif;
  }
  .sheet {
    position: relative;
    width: 1200px;
    height: 1200px;
  }
  .card {
    position: absolute;
    left: 150px;
    width: 900px;
    height: 514px;
    background: var(--card-bg);
    color: var(--card-text);
    box-shadow: 0 6px 18px rgba(0,0,0,0.18);
    overflow: hidden;
  }
  .card--front { top: 70px; }
  .card--back { top: 616px; }

  /* Brand lockup */
  .brand {
    position: absolute;
    display: flex;
    flex-direction: column;
  }
  .brand__row {
    display: flex;
    align-items: center;
  }
  .brand__mark {
    background: var(--accent-teal);
    flex: none;
  }
  .brand__name {
    font-weight: 700;
    letter-spacing: 0.04em;
    text-transform: uppercase;
    line-height: 1;
  }
  .brand__tagline {
    font-weight: 700;
    line-height: 1.2;
  }

  .card--front .brand { left: 200px; top: 200px; }
  .card--front .brand__mark { width: 70px; height: 70px; margin-right: 26px; }
  .card--front .brand__name { font-size: 74px; }
  .card--front .brand__tagline { font-size: 26px; margin-left: 96px; margin-top: 10px; }

  .card--back .brand { right: 90px; top: 250px; }
  .card--back .brand__mark { width: 40px; height: 40px; margin-right: 14px; }
  .card--back .brand__name { font-size: 40px; }
  .card--back .brand__tagline { font-size: 14px; margin-left: 54px; margin-top: 6px; }

  /* Contact block */
  .contact {
    position: absolute;
    left: 60px;
    top: 48px;
    font-size: 22px;
    line-height: 1.25;
  }
  .contact__company {
    font-size: 30px;
    letter-spacing: 0.03em;
    text-transform: uppercase;
  }
  .contact__group + .contact__group { margin-top: 48px; }
  .contact p { margin: 0; }
</style>
</head>
<body>
<main class="sheet">

  <section class="card card--front" aria-label="Card front">
    <div class="brand">
      <div class="brand__row">
        <span class="brand__mark" aria-hidden="true"></span>
        <span class="brand__name">Harborline</span>
      </div>
      <span class="brand__tagline">Revenue Management Solutions</span>
    </div>
  </section>

  <section class="card card--back" aria-label="Card back">
    <div class="contact">
      <div class="contact__group">
        <p class="contact__company">Harborline</p>
        <p>Revenue Management Solutions LLC</p>
        <p>www.HarborlineRMS.com</p>
      </div>
      <div class="contact__group">
        <p>Dana Whitlow</p>
        <p>Regional Revenue Manager</p>
        <p>Office 555-014-2290</p>
        <p>Fax 555-014-3381</p>
        <p>Dana@HarborlineRMS.com</p>
      </div>
    </div>
    <div class="brand">
      <div class="brand__row">
        <span class="brand__mark" aria-hidden="true"></span>
        <span class="brand__name">Harborline</span>
      </div>
      <span class="brand__tagline">Revenue Management Solutions</span>
    </div>
  </section>

</main>
</body>
</html>
```